Lumora Flow Collective Business Cards

I need business cards for staff in a new startup. Our company name is MorvaLeap - we train Tai Chi teachers. But our biggest project is called Lumora Flow Collective - a federal project to put together free Tai Chi classes for Vets all across America. It's a young company, with a spirit of excitement, passion, a desire to do good for others (our Vets) and a modern style and sensibility. In other words, not old-fashioned Asian martial arts theme, but something new.

Industry/Entity Type

Health And Wellness

Contact Information for Business Card

The topic is ancient healing, but the company is the Quibbletons - so I'd like a card design that captures that.

Font styles to use
Sans Serif

Colors

Designer to choose colors to be used in the design.

Requirements
Nice to have
• I've got two logos - one for the company and one for the project. I want to see if we can incorporate them both without it becoming too busy.
Should not have
• Overly old-fashioned yin-yang themes.

```html
<!DOCTYPE html>
<html lang="en">
<head>
<meta charset="utf-8">
<title>Lumora Flow Collective – Business Cards</title>
<link rel="stylesheet" href="https://fonts.googleapis.com/css2?family=Tenor+Sans&family=Arimo:wght@400&display=swap">
<style>
  :root {
    --backdrop: #6e5439;
    --card-white: #ffffff;
    --rose: #e8444f;
    --plum: #8a3a6a;
    --indigo: #2d2a6b;
    --navy: #2a2f72;
    --ink: #111111;
    --rule: rgba(255,255,255,0.7);
  }
  * { box-sizing: border-box; margin: 0; padding: 0; }
  html, body { width: 900px; height: 1200px; overflow: hidden; }
  body {
    background: var(--backdrop);
    position: relative;
    font-family: "Tenor Sans", sans-serif;
  }
  .card {
    position: absolute;
    left: 90px;
    width: 720px;
    box-shadow: 0 10px 22px rgba(0,0,0,0.45);
    overflow: hidden;
  }
  /* Front */
  .card--front {
    top: 133px;
    height: 422px;
    background: linear-gradient(180deg, var(--rose) 0%, var(--plum) 50%, var(--indigo) 100%);
    color: var(--card-white);
  }
  .holder { position: absolute; left: 48px; top: 78px; }
  .holder__name { font-size: 19px; letter-spacing: 0.5px; text-transform: uppercase; line-height: 1.1; }
  .holder__role { font-size: 15px; text-transform: uppercase; opacity: 0.95; margin-top: 4px; }
  .brand {
    position: absolute;
    right: 48px;
    top: 90px;
    display: flex;
    align-items: center;
    gap: 14px;
  }
  .brand__dot {
    width: 60px; height: 60px;
    border: 3px solid currentColor;
    border-radius: 50%;
  }
  .brand__name { font-size: 25px; letter-spacing: 0.5px; text-transform: uppercase; line-height: 1; }
  .card__rule {
    position: absolute;
    left: 48px; right: 48px; top: 268px;
    height: 1px; background: var(--rule);
  }
  .contacts {
    position: absolute; left: 48px; top: 284px;
    list-style: none;
    font-family: "Arimo", sans-serif;
    font-size: 15px;
  }
  .contacts li { display: flex; align-items: center; gap: 8px; height: 22px; }
  .contacts svg { width: 15px; height: 15px; fill: var(--rose); }
  .address {
    position: absolute; right: 48px; top: 284px;
    font-family: "Arimo", sans-serif; font-size: 15px;
    text-align: right; line-height: 22px;
  }
  /* Back */
  .card--back {
    top: 637px;
    height: 418px;
    background: var(--card-white);
  }
  .back-brands {
    position: absolute; left: 0; right: 0; top: 120px;
    display: flex; justify-content: center; align-items: center; gap: 60px;
  }
  .back-brand { display: flex; align-items: center; gap: 12px; }
  .back-brand__dot { width: 54px; height: 54px; border-radius: 50%; }
  .back-brand--company { color: var(--rose); }
  .back-brand--company .back-brand__dot { background: var(--rose); }
  .back-brand--project { color: var(--navy); }
  .back-brand--project .back-brand__dot { border: 3px solid var(--navy); }
  .back-brand__name { font-size: 26px; text-transform: uppercase; letter-spacing: 0.5px; }
  .wave { position: absolute; left: 0; top: 0; width: 720px; height: 418px; }
  .tagline {
    position: absolute; left: 0; right: 0; top: 374px;
    text-align: center; color: var(--card-white);
    font-size: 15px; letter-spacing: 0.2px;
  }
</style>
</head>
<body>

<section class="card card--front">
  <div class="holder">
    <p class="holder__name">Corwin Vale</p>
    <p class="holder__role">CEO/Founder</p>
  </div>

  <div class="brand">
    <span class="brand__dot"></span>
    <span class="brand__name">Lumora Flow<br>Collective</span>
  </div>

  <div class="card__rule"></div>

  <ul class="contacts">
    <li><svg viewBox="0 0 16 16"><path d="M3 1l3 3-2 2c1 2 3 4 5 5l2-2 3 3-2 3C7 14 2 9 1 4z"/></svg>555 014 2738</li>
    <li><svg viewBox="0 0 16 16"><path d="M4 1h8v4H4zM1 6h14v6h-3v3H4v-3H1zM5 10v4h6v-4z"/></svg>555 014 2738</li>
    <li><svg viewBox="0 0 16 16"><path d="M1 3h14v10H1zM2 4l6 5 6-5v1L8 10 2 5z" fill-rule="evenodd"/></svg>corwin@lumoraflow.org</li>
    <li><svg viewBox="0 0 16 16"><path d="M8 1a7 7 0 100 14A7 7 0 008 1zm0 1.5c.8 1 1.4 2.4 1.6 4.5H6.4C6.6 4.9 7.2 3.5 8 2.5zM2.6 7a5.5 5.5 0 012.9-4c-.6 1.2-1 2.5-1.1 4zm0 2h1.8c.1 1.5.5 2.8 1.1 4a5.5 5.5 0 01-2.9-4zM8 13.5c-.8-1-1.4-2.4-1.6-4.5h3.2c-.2 2.1-.8 3.5-1.6 4.5zm2.5-.5c.6-1.2 1-2.5 1.1-4h1.8a5.5 5.5 0 01-2.9 4zm1.1-6c-.1-1.5-.5-2.8-1.1-4a5.5 5.5 0 012.9 4z"/></svg>www.lumoraflow.org</li>
  </ul>

  <address class="address" style="font-style:normal">
    418 Harrow Lane SE<br>
    Suite 210, Pellbrook<br>
    MN 55410
  </address>
</section>

<section class="card card--back">
  <svg class="wave" viewBox="0 0 720 418" aria-hidden="true">
    <defs>
      <linearGradient id="bandFade" x1="0" x2="1" y1="0" y2="0">
        <stop offset="0" stop-color="#000000"/>
        <stop offset="0.45" stop-color="#7a2028"/>
        <stop offset="0.75" stop-color="#e8444f"/>
        <stop offset="1" stop-color="#e8444f"/>
      </linearGradient>
    </defs>
    <path d="M0 326 C150 300 300 312 420 332 S640 336 720 300 L720 418 L0 418 Z" fill="url(#bandFade)"/>
    <path d="M380 334 C500 334 620 318 720 286 L720 300 C620 334 500 344 380 334 Z" fill="#e8444f"/>
  </svg>

  <div class="back-brands">
    <div class="back-brand back-brand--company">
      <span class="back-brand__dot"></span>
      <span class="back-brand__name">MorvaLeap</span>
    </div>
    <div class="back-brand back-brand--project">
      <span class="back-brand__dot"></span>
      <span class="back-brand__name">Lumora Flow<br>Collective</span>
    </div>
  </div>

  <p class="tagline">Federal project to put together free Tai Chi classes for Vets all across America.</p>
</section>

</body>
</html>
```